Kindro - Bringing Warmth and Quality to Senior Living

We are a new company based in Sydney, Australia. We have developed a state-of-the-art app for communication between aged care facilities and families.

Kindro has been developed for facilities to augment the best possible care by providing easy, safe and secure communication for families to stay in touch with their loved ones.
Updates

the website needs to be designed so we can add functionality including multilingual support. display in different languages.we also require enquiry and email/data base function. we want it simple and clean so its responsive. the target audience will be 40+ in age. there will be a video on home page. would like to start with 6 pages/ subjects -homepage -about us -our solution -demonstration page, this will be a page that contains videos of people using our product -customer testimonials -contact us

Target Market(s)

Aged care facilities.
Families (over 40’s age group) who are looking for a facility for their loved ones.

Number of Pages Required

5+ page

Font styles to use
Sans Serif

Colors
faa54b
ffffff
0255a3

Requirements
Must have
• - Our corporate colour is #EE8811.
• - If you're using stock photography, please use brimlo prints photos as we have a license for their photos.
• - The design needs to be responsive (mobile and desktop)
• -White space on each page
Nice to have
• -need to leave a place for a future animation video to be added in on the home tab
Should not have
• we don't want flash technology

```html
<!DOCTYPE html>
<html lang="en">
<head>
<meta charset="utf-8">
<title>Kindro - Bringing Warmth and Quality to Senior Living</title>
<link href="https://fonts.googleapis.com/css2?family=Lato:wght@300;400;700&family=Roboto:wght@400;500&display=swap" rel="stylesheet">
<style>
:root{
  --brand-orange:#ee8811;
  --soft-orange:#faa54b;
  --brand-blue:#0255a3;
  --white:#ffffff;
  --ink:#4a4a4a;
  --muted:#6b6b6b;
  --nav-ink:#555e68;
  --tick-green:#5cb85c;
}
*{box-sizing:border-box;margin:0;padding:0}
html,body{width:1200px;height:2326px;overflow:hidden}
body{font-family:'Lato',sans-serif;color:var(--ink);background:var(--white);position:relative}
.brand{display:flex;align-items:center;gap:6px;color:var(--brand-orange);font-weight:700;font-family:'Lato',sans-serif;white-space:nowrap}
.brand-dot{width:22px;height:22px;border-radius:50%;background:var(--brand-orange)}

/* header */
.site-header{position:absolute;top:0;left:0;width:1200px;height:72px}
.site-header .brand{position:absolute;left:108px;top:22px;font-size:26px}
.site-header .brand-dot{width:26px;height:26px}
.main-nav{position:absolute;left:427px;top:30px;width:498px;display:flex;justify-content:space-between;font-size:11.5px;color:var(--nav-ink);white-space:nowrap}
.btn-header{position:absolute;left:946px;top:14px;width:146px;height:45px;border-radius:23px;background:var(--brand-blue);color:var(--white);font-size:12px;display:flex;align-items:center;justify-content:center}

/* hero */
.hero{position:absolute;top:72px;left:0;width:1200px;height:650px;background:linear-gradient(100deg,#5b5552 0%,#7b7370 40%,#8a8682 65%,#6d6b6c 100%);color:var(--white);text-align:center}
.hero-title{position:absolute;top:108px;left:0;width:1200px;font-weight:300;font-size:40px;line-height:62px}
.play-btn{position:absolute;left:548px;top:276px;width:100px;height:100px}
.signup-label{position:absolute;top:458px;left:0;width:1164px;font-size:12px;font-weight:700}
.signup-form{position:absolute;top:490px;left:318px;display:flex}
.signup-form .field{width:184px;height:45px;background:var(--white);color:#a0a0a0;font-size:13px;display:flex;align-items:center;padding-left:14px;text-align:left;border-right:1px solid #ddd}
.signup-form .submit{width:197px;height:45px;background:var(--brand-blue);color:var(--white);font-size:11.5px;font-weight:700;display:flex;align-items:center;justify-content:center}
.fine-print{position:absolute;top:545px;left:0;width:1200px;font-size:9.5px}
.fine-print b{font-weight:700}

/* about */
.about{position:absolute;top:722px;left:0;width:1200px;height:482px;display:flex}
.about-photo{width:635px;height:482px;background:linear-gradient(160deg,#5f7d3c 0%,#8aa65a 35%,#b58a60 65%,#6b5f58 100%)}
.about-panel{flex:1;background:var(--brand-blue);color:var(--white);padding:170px 0 0 58px}
.about-panel h2{font-weight:300;font-size:31px;margin-bottom:22px}
.about-panel p{font-size:13.5px;line-height:20px;width:385px}

/* why */
.why{position:absolute;top:1204px;left:0;width:1200px;height:463px}
.why h2{position:absolute;left:238px;top:84px;font-weight:300;font-size:31px;color:#444}
.why-list{position:absolute;left:238px;top:142px;list-style:none;width:414px}
.why-list li{display:flex;gap:15px;font-size:12.8px;line-height:20px;color:#555;margin-bottom:20px}
.why-list li svg{flex:none}
.app-screen{position:absolute;left:749px;top:42px;width:204px;height:393px;border-radius:14px;background:linear-gradient(180deg,#f2f2f2 0%,#e9e9e9 38%,#c98a6a 55%,#6f7d4a 70%,#e8918b 82%,#f4f4f4 100%)}

/* cta */
.cta{position:absolute;top:1667px;left:0;width:1200px;height:356px;background:linear-gradient(90deg,#f2a044 0%,var(--soft-orange) 50%,#f39a3e 100%);text-align:center;color:var(--white)}
.cta h2{position:absolute;top:103px;left:0;width:1200px;font-weight:300;font-size:50px}
.cta p{position:absolute;top:173px;left:0;width:1200px;font-size:18px}
.btn-cta{position:absolute;left:489px;top:228px;width:222px;height:70px;background:var(--brand-blue);color:var(--white);font-size:26px;display:flex;align-items:center;justify-content:center}

/* footer */
.site-footer{position:absolute;top:2023px;left:0;width:1200px;height:303px}
.site-footer .brand{position:absolute;left:137px;top:86px;font-size:18px}
.site-footer .brand-dot{width:18px;height:18px}
.footer-about{position:absolute;left:137px;top:117px;width:345px;font-size:12.2px;line-height:23.5px;color:var(--muted);font-weight:300}
.footer-links{position:absolute;top:119px;display:flex;flex-direction:column;gap:12px;font-family:'Roboto',sans-serif;font-size:12.5px;line-height:15px;color:#444}
.social{position:absolute;left:137px;top:213px;display:flex;gap:5px}
.social span{width:23px;height:23px;background:var(--brand-blue);border-radius:2px}
</style>
</head>
<body>

<header class="site-header">
  <div class="brand"><span class="brand-dot"></span>Kindro</div>
  <nav class="main-nav">
    <span>HOME</span><span>ABOUT US</span><span>OUR SOLUTION</span><span>TESTIMONIALS</span><span>CONTACT</span><span>OUR TEAM</span>
  </nav>
  <div class="btn-header">Get Started</div>
</header>

<section class="hero" role="img" aria-label="Photo of a nurse serving tea to an elderly resident, darkened behind the headline">
  <h1 class="hero-title">Solution that provides communication between<br>aged care facilities, residents and families</h1>
  <svg class="play-btn" viewBox="0 0 100 100" aria-label="Play video">
    <circle cx="50" cy="50" r="50" fill="#fff"/>
    <path d="M42 34 L68 50 L42 66 Z" fill="#111"/>
  </svg>
  <div class="signup-label">SIGN UP NOW FOR A FREE QUOTE</div>
  <div class="signup-form">
    <div class="field">Your Name</div>
    <div class="field">Email Address</div>
    <div class="submit">START YOUR FREE TRIAL</div>
  </div>
  <div class="fine-print">* We don't share your personal info with anyone. Check out our Privacy Policy <b>for more information.</b></div>
</section>

<section class="about">
  <div class="about-photo" role="img" aria-label="Photo of elderly residents and a carer playing cards at an outdoor table under trees"></div>
  <div class="about-panel">
    <h2>What is Kindro?</h2>
    <p>Kindro is a state-of-the-art solution that provides communication between aged care facilities, residents and families. Kindro has been developed for facilities to augment the best possible care by providing easy, safe and secure communication for families to stay in touch with their loved ones.</p>
  </div>
</section>

<section class="why">
  <h2>WHY Kindro?</h2>
  <ul class="why-list">
    <li><svg width="21" height="21" viewBox="0 0 21 21"><circle cx="10.5" cy="10.5" r="10.5" fill="var(--tick-green)"/><path d="M6 11 L9.3 14 L15 7.5" stroke="#fff" stroke-width="2.2" fill="none"/></svg>With the spotlight on aged care, facilities need every advantaged to demonstrate excellence to residents and their families, and Kindro provide a solution.</li>
    <li><svg width="21" height="21" viewBox="0 0 21 21"><circle cx="10.5" cy="10.5" r="10.5" fill="var(--tick-green)"/><path d="M6 11 L9.3 14 L15 7.5" stroke="#fff" stroke-width="2.2" fill="none"/></svg>Reports have been so confronting within the industry that a Royal Commission into Aged Care Quality and Safety was created by the Federal Government.</li>
    <li><svg width="21" height="21" viewBox="0 0 21 21"><circle cx="10.5" cy="10.5" r="10.5" fill="var(--tick-green)"/><path d="M6 11 L9.3 14 L15 7.5" stroke="#fff" stroke-width="2.2" fill="none"/></svg>There has never been a better time for facilities to update the provision of services through the use of technology.</li>
    <li><svg width="21" height="21" viewBox="0 0 21 21"><circle cx="10.5" cy="10.5" r="10.5" fill="var(--tick-green)"/><path d="M6 11 L9.3 14 L15 7.5" stroke="#fff" stroke-width="2.2" fill="none"/></svg>Facilities that already provide quality care can enhance and expand that care for facility management, families and residents.</li>
  </ul>
  <div class="app-screen" role="img" aria-label="Image of the app's meal report screen on a phone, with sliders and a photo of a plated meal"></div>
</section>

<section class="cta" role="img" aria-label="Orange-tinted photo of a carer holding an elderly person's hands">
  <h2>Get Aged Care Quality and Safety</h2>
  <p>Start today with a free 30 day trial - No credit card required.</p>
  <div class="btn-cta">GET STARTED</div>
</section>

<footer class="site-footer">
  <div class="brand"><span class="brand-dot"></span>Kindro</div>
  <p class="footer-about">We are a new company based in Sydney, Australia. We have developed a state-ofthe-art app for communication between aged care facilities and families.</p>
  <div class="footer-links" style="left:611px"><span>About</span><span>Careers</span><span>Contact</span></div>
  <div class="footer-links" style="left:769px"><span>Features</span><span>Pricing</span><span>Security</span></div>
  <div class="footer-links" style="left:928px"><span>Help Center</span><span>API</span><span>FAQ</span></div>
  <div class="social"><span></span><span></span><span></span><span></span></div>
</footer>

</body>
</html>
```